Bright, Fun and hard to forget home inspection business card.

We need a Business card design for a new Home Inspection company. We are building a brand that is bright, fun and easy to remember.

Target Market(s)

Anyone involed in buying and selling of homes.

Industry/Entity Type

Home Inspection

Contact Information for Business Card

Colin Hartwell Owner/Inspector

Wedsite- KestrelHouseCheck.example
Phone: 253-555-0147
Email- ColinHartwell@mailbox.example
WA Lic # 4738

Requirements
Must have
• BQRV LOGO somewhere on card.

```html
<!DOCTYPE html>
<html lang="en">
<head>
<meta charset="utf-8">
<title>Kestrel House Check – Business Card</title>
<link href="https://fonts.googleapis.com/css2?family=Mulish:wght@400;600;700;800&display=swap" rel="stylesheet">
<style>
  :root {
    --backdrop: #2b2b2b;
    --card-white: #f6f6f6;
    --brand-orange: #e4562c;
    --brand-orange-deep: #cf4822;
    --ink-grey: #4a4a4a;
    --soft-grey: #8d8d8d;
    --mist-grey: #c9c9c9;
    --text-light: #ffffff;
    --tint-light: #fbe3d9;
  }
  * { box-sizing: border-box; margin: 0; padding: 0; }
  html, body {
    width: 1200px; height: 873px; overflow: hidden;
    background: var(--backdrop);
    font-family: "Mulish", sans-serif;
  }
  .canvas { position: relative; width: 1200px; height: 873px; }

  /* ---------- Front card (portrait) ---------- */
  .card-front {
    position: absolute; left: 130px; top: 130px;
    width: 350px; height: 612px;
    background: var(--card-white);
    overflow: hidden;
    box-shadow: 0 14px 30px rgba(0,0,0,.5);
  }
  .holder { text-align: center; padding-top: 46px; }
  .holder-name { font-weight: 800; font-size: 25px; color: var(--soft-grey); }
  .holder-role { font-weight: 400; font-size: 16px; color: var(--soft-grey); margin-top: 2px; }

  .brand-mark {
    display: flex; align-items: center; justify-content: center; gap: 10px;
    margin-top: 30px;
  }
  .brand-dot { width: 16px; height: 16px; border-radius: 50%; background: var(--brand-orange); }
  .brand-name {
    font-weight: 800; font-size: 27px; line-height: 1.02;
    letter-spacing: .5px; text-transform: uppercase;
  }
  .card-front .brand-name { color: var(--ink-grey); }

  .city-skyline {
    position: absolute; left: 0; top: 258px; width: 100%; height: 130px;
    background: linear-gradient(180deg, var(--card-white) 0%, var(--mist-grey) 45%, var(--brand-orange) 100%);
  }
  .contact-band {
    position: absolute; left: 0; top: 388px; width: 100%; bottom: 0;
    background: linear-gradient(180deg, var(--brand-orange) 0%, var(--brand-orange-deep) 100%);
    padding: 34px 0 0 36px;
  }
  .contact-list { list-style: none; }
  .contact-item {
    display: flex; align-items: center; gap: 16px;
    color: var(--tint-light); font-size: 15px; font-weight: 600;
    height: 50px;
  }
  .contact-icon { width: 26px; height: 26px; flex: none; }

  /* ---------- Back card (landscape) ---------- */
  .card-back {
    position: absolute; left: 540px; top: 260px;
    width: 612px; height: 350px;
    background: linear-gradient(135deg, var(--brand-orange) 0%, var(--brand-orange-deep) 100%);
    box-shadow: 0 14px 30px rgba(0,0,0,.5);
    overflow: hidden;
  }
  .services {
    position: absolute; left: 40px; top: 150px; list-style: none;
  }
  .service {
    color: var(--text-light); font-weight: 800; font-size: 16px;
    letter-spacing: .8px; text-transform: uppercase; height: 38px;
    display: flex; align-items: center; gap: 10px;
  }
  .service::before {
    content: ""; width: 6px; height: 6px; border-radius: 50%;
    background: var(--text-light); flex: none;
  }
  .card-back .brand-mark {
    position: absolute; right: 40px; top: 62px; margin: 0;
    justify-content: flex-end;
  }
  .card-back .brand-name { color: var(--text-light); font-size: 30px; text-align: left; }
  .card-back .brand-dot { background: var(--text-light); width: 20px; height: 20px; }

  .licence {
    position: absolute; right: 86px; bottom: 66px;
    color: var(--ink-grey); font-size: 14px; font-weight: 600;
  }
  .cert-badge {
    position: absolute; right: 40px; bottom: 58px;
    width: 34px; height: 34px; background: var(--ink-grey); border: 3px solid var(--text-light);
  }
</style>
</head>
<body>
<main class="canvas">

  <section class="card-front" aria-label="Business card front">
    <header class="holder">
      <p class="holder-name">Colin Hartwell</p>
      <p class="holder-role">Owner/Inspector</p>
    </header>

    <div class="brand-mark">
      <span class="brand-dot"></span>
      <p class="brand-name">Kestrel<br>House Check<br>LLC</p>
    </div>

    <div class="city-skyline" role="img" aria-label="Orange city skyline silhouette with a tower and a grey mountain behind"></div>

    <div class="contact-band">
      <ul class="contact-list">
        <li class="contact-item">
          <svg class="contact-icon" viewBox="0 0 26 26" aria-hidden="true">
            <path d="M4 9c0-2 2-4 9-4s9 2 9 4v2h-4V9H8v2H4z" fill="var(--tint-light)"/>
            <rect x="6" y="12" width="14" height="9" rx="2" fill="var(--tint-light)"/>
          </svg>
          <span>253-555-0147</span>
        </li>
        <li class="contact-item">
          <svg class="contact-icon" viewBox="0 0 26 26" aria-hidden="true">
            <rect x="2" y="6" width="22" height="15" fill="none" stroke="var(--tint-light)" stroke-width="2"/>
            <path d="M2 6l11 9 11-9" fill="none" stroke="var(--tint-light)" stroke-width="2"/>
          </svg>
          <span>info@KestrelHouseCheck.example</span>
        </li>
        <li class="contact-item">
          <svg class="contact-icon" viewBox="0 0 26 26" aria-hidden="true">
            <circle cx="13" cy="13" r="11" fill="none" stroke="var(--tint-light)" stroke-width="2"/>
            <ellipse cx="13" cy="13" rx="5" ry="11" fill="none" stroke="var(--tint-light)" stroke-width="1.6"/>
            <path d="M2 13h22" stroke="var(--tint-light)" stroke-width="1.6"/>
          </svg>
          <span>www.KestrelHouseCheck.example</span>
        </li>
      </ul>
    </div>
  </section>

  <section class="card-back" aria-label="Business card back">
    <div class="brand-mark">
      <span class="brand-dot"></span>
      <p class="brand-name">Kestrel<br>House Check<br>LLC</p>
    </div>

    <ul class="services">
      <li class="service">Buyer &amp; Seller Inspection</li>
      <li class="service">11 Month Warrenty Inspection</li>
      <li class="service">Maintenance Inspections.</li>
      <li class="service">On Site Reporting</li>
    </ul>

    <p class="licence">WA Lic # 4738</p>
    <span class="cert-badge" aria-label="Certification badge"></span>
  </section>

</main>
</body>
</html>
```